Poster Title Design

Create a text design concept for a documentary film called:
"The Orchard Beekeepers"
Background should be black, design elements and text should be red and/or white.
Design should be bold and readable from a distance.
Please provide at least 3 alternative concepts per submission.
(No need to include images or illustrations in the design. We only need a text treatment with optional simple graphic lines curves or blocks. There are no existing show logos.)
Please submit concepts centered in frame, 1200 wide x 1000 high jpg.
Thanks!
Good Luck!
- please use solid read and white colors for text and design elements.
- please do not use any fonts in the courier family.
please do not use any script or shadow fonts.
please do not use any other colors than red, white and black.
please avoid using gradients.
no need to include images or illustrations, just need the title text treatment.

```html
<!DOCTYPE html>
<html lang="en">
<head>
<meta charset="utf-8">
<title>The Orchard Beekeepers — Title Treatment</title>
<link rel="stylesheet" href="https://fonts.googleapis.com/css2?family=Alfa+Slab+One&display=swap">
<style>
  :root {
    --page: #ffffff;
    --band-black: #000000;
    --title-red: #ff0000;
    --reflection-line: #ffffff;
  }
  html, body {
    margin: 0;
    padding: 0;
    width: 1200px;
    height: 900px;
    overflow: hidden;
    background: var(--page);
  }
  .poster {
    position: relative;
    width: 1200px;
    height: 900px;
    background: var(--page);
  }
  .title-band {
    position: absolute;
    left: 0;
    top: 60px;
    width: 1200px;
    height: 745px;
    background: var(--band-black);
  }
  .title-art {
    position: absolute;
    left: 0;
    top: 0;
    width: 1200px;
    height: 900px;
  }
  .title-text {
    font-family: "Alfa Slab One", "Rockwell", serif;
    font-size: 400px;
    word-spacing: 60px;
  }
  .title-main { fill: var(--title-red); }
  .title-reflection {
    fill: var(--band-black);
    stroke: var(--reflection-line);
    stroke-width: 2;
  }
</style>
</head>
<body>
  <main class="poster">
    <div class="title-band"></div>
    <svg class="title-art" viewBox="0 0 1200 900" xmlns="http://www.w3.org/2000/svg">
      <g transform="translate(0,900) scale(1,-1)" aria-hidden="true">
        <text class="title-text title-reflection" x="82" y="440" textLength="1070" lengthAdjust="spacingAndGlyphs">THE ORCHARD BEEKEEPERS</text>
      </g>
      <text class="title-text title-main" x="82" y="440" textLength="1070" lengthAdjust="spacingAndGlyphs">THE ORCHARD BEEKEEPERS</text>
    </svg>
  </main>
</body>
</html>
```